名刺を新しく作ろうと考えています。基本的にはシンプルなものをと考えておりますが、花農家なので
背景に花をイメージした模様とかイラストなど特に指定はありませんので色々提案して頂けるとありがたいです。

表面:会社名/名前/住所/電話/Fax/携帯電話番号
裏面:無地
緑、ピンク、黄
名刺の詳細を追記します。
会社名:杉野園芸
名前:杉野健太
住所:781-0342島根県出雲市桜木町517
TEL:(0853)47-1286
FAX:(0853)47-1286
携帯:***-****-****

特にデザインの指定はありませんので自由に提案して頂けると助かります。
よろしくお願い致します。
弊社の主力品種であるあじさいの「夕凪草」の写真のデータがありましたので
追記で載せさせて頂きます。
この品種の最大の特徴はストライプが入るところなので、そのあたりを
デザインに活かしてもらえると喜びます。
大変に遅くなって申し訳ありませんが、よろしくお願いします。
先程の写真はピンクでしたが同じ「夕凪草」でこちらはブルーです。

一目見て夕凪草の良さが伝わって来ていると強く感じました。
また全体的な色使いのバランスも良く自分のイメージに限りなく近かったのがポイントです。

ご提案頂きましたノヴァーの皆様へ

今回は当社の名刺製作に多数のご提案を頂きまして誠に有難うございます。
なんら具体的なイメージもなくノヴァーの皆様の頭を悩ませたこと大変申し訳ありません。にもかかわらず素晴らしい作品の数々ただただ感謝に尽きます。
これからもノヴァーの皆様のご活躍をお祈りしております。

```html
<!DOCTYPE html>
<html lang="ja">
<head>
<meta charset="utf-8">
<title>杉野園芸 名刺</title>
<link rel="stylesheet" href="https://fonts.googleapis.com/css2?family=Shippori+Mincho+B1:wght@500;700;800&display=swap">
<style>
  :root {
    --leaf-dark: #0e1a12;
    --leaf-mid: #24392a;
    --petal-blue: #8f9fe0;
    --petal-lilac: #b7b3ec;
    --petal-pale: #e4e4f8;
    --ink-light: #ffffff;
    --ink-dark: #1b1f3a;
    --glow: rgba(255, 255, 255, 0.9);
  }
  html, body {
    margin: 0;
    padding: 0;
    width: 726px;
    height: 1200px;
    overflow: hidden;
    background: #ffffff;
  }
  .card {
    position: relative;
    width: 726px;
    height: 1200px;
    overflow: hidden;
    font-family: "Shippori Mincho B1", serif;
  }
  .hydrangea-photo {
    position: absolute;
    inset: 0;
    background:
      radial-gradient(ellipse 55% 40% at 80% 82%, var(--petal-lilac) 0%, var(--petal-blue) 45%, rgba(143,159,224,0) 75%),
      radial-gradient(ellipse 45% 35% at 12% 62%, var(--petal-pale) 0%, rgba(183,179,236,0.85) 40%, rgba(143,159,224,0) 75%),
      radial-gradient(ellipse 40% 25% at 18% 8%, rgba(120,130,170,0.55) 0%, rgba(120,130,170,0) 70%),
      radial-gradient(ellipse 30% 22% at 95% 28%, rgba(110,120,160,0.45) 0%, rgba(110,120,160,0) 70%),
      linear-gradient(180deg, var(--leaf-mid) 0%, var(--leaf-dark) 35%, #1a2a1f 55%, #3a4a6a 100%);
  }
  .tagline {
    position: absolute;
    top: 20px;
    right: 8px;
    writing-mode: vertical-rl;
    font-size: 29px;
    font-weight: 500;
    line-height: 49px;
    letter-spacing: 2px;
    color: var(--ink-light);
    text-shadow: 0 0 6px rgba(0,0,0,0.6);
    margin: 0;
  }
  .company {
    position: absolute;
    top: 48px;
    left: 423px;
    writing-mode: vertical-rl;
    font-size: 36px;
    font-weight: 700;
    letter-spacing: 3px;
    color: var(--ink-light);
    text-shadow: 0 0 6px rgba(0,0,0,0.6);
    margin: 0;
  }
  .name-part {
    position: absolute;
    writing-mode: vertical-rl;
    font-size: 62px;
    font-weight: 800;
    letter-spacing: 6px;
    color: var(--ink-light);
    text-shadow: 0 0 8px rgba(0,0,0,0.6);
  }
  .name-family { top: 100px; left: 349px; }
  .name-given { top: 330px; left: 521px; }
  .postal {
    position: absolute;
    top: 500px;
    left: 44px;
    font-size: 27px;
    font-weight: 700;
    color: var(--ink-dark);
    text-shadow: 0 0 6px var(--glow), 0 0 10px var(--glow);
    margin: 0;
  }
  .contact {
    position: absolute;
    top: 552px;
    right: 472px;
    writing-mode: vertical-rl;
    text-orientation: upright;
    font-size: 27px;
    font-weight: 700;
    line-height: 48px;
    color: var(--ink-dark);
    text-shadow: 0 0 6px var(--glow), 0 0 10px var(--glow);
    margin: 0;
  }
  .contact span { display: block; }
</style>
</head>
<body>
  <div class="card">
    <div class="hydrangea-photo" role="img" aria-label="ストライプ模様の青いあじさい「夕凪草」が咲く写真"></div>

    <p class="tagline">心をこめて<br>育てています。</p>

    <h1 class="company">杉野園芸</h1>
    <div class="name">
      <span class="name-part name-family">杉野</span>
      <span class="name-part name-given">健太</span>
    </div>

    <p class="postal">〒781-0342</p>
    <p class="contact">
      <span class="address">島根県出雲市桜木町517</span>
      <span class="tel">TEL（0853）47ー1286</span>
      <span class="fax">FAX（0853）47ー1286</span>
      <span class="mobile">携帯090ー○○○○ー○○○○</span>
    </p>
  </div>
</body>
</html>
```